Business Card Design - Local Discount Club

Looking for a fun business card for a local discount club. One side should be the logo only and the other should be have :

Name
Title
Phone, Email
Website

```html
<!DOCTYPE html>
<html lang="en">
<head>
<meta charset="UTF-8">
<title>Tidewater Savers – Business Card</title>
<link href="https://fonts.googleapis.com/css2?family=Poppins:wght@400;600;700&display=swap" rel="stylesheet">
<style>
  :root {
    --page-bg: #121213;
    --card-bg: #2a2a2c;
    --brand-blue: #3a5bd0;
    --accent-cyan: #3ec8e6;
    --text-light: #d8d8dc;
    --dot-teal: #3d5a5c;
    --dot-olive: #3f4a36;
    --dot-navy: #30374f;
    --disc-dark: #2e2e30;
    --disc-mid: #4a4a4c;
    --disc-light: #5a5a5c;
  }
  * { margin: 0; padding: 0; box-sizing: border-box; }
  html, body { width: 1200px; height: 820px; overflow: hidden; }
  body {
    background: var(--page-bg);
    font-family: "Poppins", sans-serif;
    position: relative;
  }
  .card {
    position: absolute;
    left: 290px;
    width: 620px;
    height: 354px;
    background: var(--card-bg);
    border-left: 3px solid var(--brand-blue);
    border-bottom: 3px solid var(--brand-blue);
    overflow: hidden;
  }
  .card--front { top: 36px; }
  .card--back { top: 430px; }

  .dot { position: absolute; border-radius: 50%; }
  .dot--teal { left: 72px; top: 38px; width: 46px; height: 46px; background: var(--dot-teal); }
  .dot--olive { left: 32px; top: 100px; width: 32px; height: 32px; background: var(--dot-olive); }
  .dot--navy { left: 86px; top: 96px; width: 66px; height: 66px; background: var(--dot-navy); }

  .brand {
    position: absolute;
    display: flex;
    align-items: center;
    gap: 10px;
    color: var(--brand-blue);
    font-weight: 700;
    white-space: nowrap;
  }
  .brand__mark { border-radius: 50%; background: var(--brand-blue); flex: none; }
  .card--front .brand { right: 34px; top: 82px; font-size: 34px; }
  .card--front .brand__mark { width: 16px; height: 16px; }
  .card--back .brand { right: 30px; top: 150px; font-size: 28px; }
  .card--back .brand__mark { width: 13px; height: 13px; }

  .divider {
    position: absolute;
    left: 118px;
    right: 30px;
    top: 244px;
    height: 1px;
    background: var(--accent-cyan);
  }
  .person { position: absolute; left: 118px; top: 186px; }
  .person__name {
    color: var(--brand-blue);
    font-weight: 700;
    font-size: 21px;
    letter-spacing: 0.5px;
    line-height: 1.1;
  }
  .person__title { color: var(--text-light); font-size: 15px; line-height: 1.4; }

  .contacts { position: absolute; left: 118px; top: 262px; list-style: none; }
  .contacts li {
    display: flex;
    align-items: center;
    gap: 8px;
    color: var(--text-light);
    font-size: 16px;
    line-height: 1.5;
  }
  .contacts svg { width: 16px; height: 16px; flex: none; }

  .website {
    position: absolute;
    right: 34px;
    top: 262px;
    color: var(--text-light);
    font-size: 14px;
    letter-spacing: 0.3px;
  }

  .disc--small { left: 28px; top: 104px; width: 64px; height: 64px; background: radial-gradient(circle at 35% 30%, var(--disc-light), var(--disc-mid)); }
  .disc--top { left: 150px; top: 34px; width: 84px; height: 84px; background: var(--disc-dark); box-shadow: inset 0 1px 2px rgba(255,255,255,0.08); }
  .disc--large { left: 140px; top: 158px; width: 124px; height: 124px; background: radial-gradient(circle at 40% 30%, var(--disc-light), var(--disc-mid)); }
</style>
</head>
<body>
  <section class="card card--front" aria-label="Business card front">
    <span class="dot dot--teal"></span>
    <span class="dot dot--olive"></span>
    <span class="dot dot--navy"></span>

    <div class="brand"><span class="brand__name">Tidewater Savers</span><span class="brand__mark"></span></div>

    <div class="person">
      <p class="person__name">MARCUS BELL</p>
      <p class="person__title">Managing Director</p>
    </div>

    <div class="divider"></div>

    <ul class="contacts">
      <li>
        <svg viewBox="0 0 24 24" aria-hidden="true"><path fill="var(--brand-blue)" d="M6.6 10.8a15.1 15.1 0 0 0 6.6 6.6l2.2-2.2c.3-.3.7-.4 1-.2 1.1.4 2.3.6 3.600.6.6 0 1 .4 1 1V20c0 .6-.4 1-1 1A17 17 0 0 1 3 4c0-.6.4-1 1-1h3.5c.6 0 1 .4 1 1 0 1.3.2 2.5.6 3.6.1.3 0 .7-.2 1z"/></svg>
        <span>055-987 654 321</span>
      </li>
      <li>
        <svg viewBox="0 0 24 24" aria-hidden="true"><path fill="var(--brand-blue)" d="M2 5h20v14H2z"/><path fill="none" stroke="var(--card-bg)" stroke-width="1.6" d="M2 5l10 8 10-8M2 19l7-7M22 19l-7-7"/></svg>
        <span>hello@tidewatersavers.com</span>
      </li>
    </ul>

    <p class="website">www.tidewatersavers.com</p>
  </section>

  <section class="card card--back" aria-label="Business card back">
    <span class="dot disc--top"></span>
    <span class="dot disc--small"></span>
    <span class="dot disc--large"></span>

    <div class="brand"><span class="brand__name">Tidewater Savers</span><span class="brand__mark"></span></div>
  </section>
</body>
</html>
```